Wordpress Design For Virtual Assistant

I need a website design for my virtual assistant company, Quorvane. I would like to have a landing page, an about page, a page to list my services, contact us and FAQ. a blog page would be great as well.

It needs to be a modern, professional but fun look. Simple and easy to read and navigate. Colors used need to match the logo colors exactly with the red color being used only as a highlight/accept color.

I have uploaded an overview of Quorvane as well as my logo, copy of business card and stationary to give you an idea of the design style I prefer.

Industry/Entity Type

It Company

Coding

Coded - Design and coding required

Font styles to use
Sans Serif

Requirements
Must have
• Color scheme with exact logo colors
Nice to have
• www.plomquest.example/ can be used as an style inspiration

```html
<!DOCTYPE html>
<html lang="en">
<head>
<meta charset="utf-8">
<title>Quorvane — Virtual Assistant Services</title>
<link rel="stylesheet" href="https://fonts.googleapis.com/css2?family=Open+Sans:wght@400;600;700&family=Anton&display=swap">
<style>
:root{
  --green:#6da523;
  --green-dark:#4f8a12;
  --red:#b5341f;
  --red-deep:#a52f1c;
  --ink:#2b2b2b;
  --text:#555;
  --line:#d8d8d8;
  --footer:#2b2b2b;
  --footer-base:#232323;
  --footer-text:#8c8c8c;
  --white:#fff;
}
*{margin:0;padding:0;box-sizing:border-box}
html,body{width:720px;height:1200px;overflow:hidden}
body{font-family:"Open Sans",Arial,sans-serif;color:var(--text);background:var(--white);position:relative}
.abs{position:absolute}

/* header */
.site-header{position:absolute;left:0;top:0;width:720px;height:86px;border-bottom:1px solid var(--line)}
.brand{left:60px;top:34px;display:flex;align-items:center;gap:6px;font-weight:700;font-size:20px;color:var(--ink)}
.brand-mark{width:10px;height:10px;background:var(--red)}
.contact-strip{top:20px;left:320px;display:flex;align-items:center;gap:10px;font-size:7px;color:var(--green)}
.contact-item{display:flex;align-items:center;gap:5px}
.icon-dot{width:20px;height:20px;border-radius:50%;background:#ececec;display:flex;align-items:center;justify-content:center}
.appointment-btn{left:542px;top:18px;width:119px;height:22px;background:linear-gradient(#78b12b,var(--green-dark));color:var(--white);font-size:7px;font-weight:700;display:flex;align-items:center;justify-content:center;gap:8px;border-radius:2px}
.main-nav{top:61px;left:289px;width:372px;display:flex;justify-content:space-between;font-size:7.5px;color:#444}
.main-nav a{color:inherit;text-decoration:none;position:relative;padding:0 15px}
.main-nav a.active{color:var(--red)}
.main-nav a.active::after{content:"";position:absolute;left:0;right:0;top:21px;height:3px;background:var(--red)}
.main-nav a:last-child{padding-right:0}

/* hero */
.hero{left:0;top:86px;width:720px;height:307px;background:radial-gradient(ellipse at 62% 45%,#34405a 0%,#1d2436 45%,#121726 100%)}
.hero-title{left:60px;top:220px;font-family:"Anton",Impact,sans-serif;font-weight:400;font-size:30px;line-height:41px;color:var(--white)}
.hero-title .g{color:var(--green)}
.hero-title .r{color:var(--red)}
.hero-arrows{left:60px;top:332px}

/* sections */
.section-title{width:720px;text-align:center;font-weight:700;font-size:16px;color:var(--ink)}
.section-lede{width:720px;text-align:center;font-size:7.5px;color:#555}
.service-card{top:490px;width:138px;text-align:center}
.service-photo{width:138px;height:96px;border:2px solid #eee}
.service-name{margin-top:12px;font-size:8.5px;font-weight:700;color:var(--red)}
.service-text{margin-top:5px;font-size:6px;line-height:13px;color:#555}
.btn-green{display:inline-block;margin-top:8px;width:63px;height:22px;line-height:22px;font-size:7px;color:var(--white);background:linear-gradient(#78b12b,var(--green-dark));border-radius:2px}

.conclusion{left:59px;top:706px;width:602px;height:79px;border:1px solid #cfcfcf}
.conclusion h3{position:absolute;left:18px;top:15px;font-size:11.5px;color:var(--red);font-weight:700}
.conclusion p{position:absolute;left:18px;top:36px;width:440px;font-size:6.8px;line-height:14.5px;color:#666}
.act-btn{position:absolute;left:479px;top:26px;width:110px;height:26px;line-height:26px;text-align:center;background:var(--red);color:var(--white);font-size:6.8px;font-weight:700;border-radius:2px}

.work-band{left:0;top:916px;width:720px;height:112px;background:var(--red)}
.work-item{top:883px;width:190px;text-align:center;color:var(--white)}
.work-ring{width:66px;height:66px;margin:0 auto;border-radius:50%;background:var(--red-deep);display:flex;align-items:center;justify-content:center}
.work-core{width:54px;height:54px;border-radius:50%;background:radial-gradient(circle at 40% 35%,#fff,#dcdcdc);display:flex;align-items:center;justify-content:center}
.work-item h4{margin-top:10px;font-size:9px;font-weight:600}
.work-item p{margin-top:5px;font-size:6.2px;line-height:13.5px}
.work-item .more{font-size:6.2px;font-weight:600;margin-top:1px}

/* footer */
.site-footer{left:0;top:1028px;width:720px;height:144px;background:var(--footer)}
.footer-base{left:0;top:1172px;width:720px;height:28px;background:var(--footer-base);text-align:center;font-size:6.5px;line-height:28px;color:#777}
.footer-col{top:1052px;font-size:6.4px;color:var(--footer-text)}
.footer-col h5{font-size:7.5px;font-weight:700;color:var(--white);margin-bottom:9px;letter-spacing:.2px}
.footer-col ul{list-style:none}
.footer-col li{line-height:15px}
.field{width:152px;height:19px;background:var(--white);border-radius:2px;margin-top:6px;padding-left:8px;font-size:6.4px;line-height:19px;color:#666}
.subscribe{margin-top:6px;width:85px;height:19px;line-height:19px;text-align:center;background:var(--green);color:var(--white);font-weight:700;font-size:6.6px;border-radius:2px}
.contact-line{display:flex;gap:8px;margin-bottom:9px;line-height:12px}
.contact-line svg{flex:none;margin-top:1px}
</style>
</head>
<body>

<header class="site-header">
  <div class="abs brand"><span class="brand-mark"></span>Quorvane</div>
  <div class="abs contact-strip">
    <span class="contact-item"><span class="icon-dot"><svg width="9" height="9" viewBox="0 0 24 24"><path d="M6.6 10.8a15 15 0 0 0 6.6 6.6l2.2-2.2a1 1 0 0 1 1-.25 11 11 0 0 0 3.6.6 1 1 0 0 1 1 1V20a1 1 0 0 1-1 1A17 17 0 0 1 3 4a1 1 0 0 1 1-1h3.5a1 1 0 0 1 1 1 11 11 0 0 0 .6 3.6 1 1 0 0 1-.25 1z" fill="#9a9a9a"/></svg></span>Call Us:(+111) 555-0192</span>
    <span class="contact-item"><span class="icon-dot"><svg width="9" height="8" viewBox="0 0 24 20"><rect x="2" y="2" width="20" height="16" rx="2" fill="none" stroke="#6da523" stroke-width="2"/><path d="M2 4l10 7 10-7" fill="none" stroke="#6da523" stroke-width="2"/></svg></span>info@quorvane.example</span>
  </div>
  <div class="abs appointment-btn">MAKE AN APPOINTMENT <svg width="6" height="4" viewBox="0 0 6 4"><path d="M0 0l3 3 3-3" fill="none" stroke="#fff" stroke-width="1"/></svg></div>
  <nav class="abs main-nav">
    <a class="active" href="#">Home</a><a href="#">About us</a><a href="#">Services</a><a href="#">FAQ</a><a href="#">Blog</a><a href="#">Contact us</a>
  </nav>
</header>

<section class="abs hero" role="img" aria-label="Photo of a businessman in a dark suit holding cupped hands with a network of people icons floating above"></section>
<h1 class="abs hero-title"><span class="g">GROW</span> YOUR <span class="r">BRAND</span><br>PRESENCE</h1>
<svg class="abs hero-arrows" width="24" height="28" viewBox="0 0 24 28"><path d="M8 1L1 14l7 13M16 1l7 13-7 13" fill="none" stroke="#8a92a6" stroke-width="1"/></svg>

<h2 class="abs section-title" style="left:0;top:413px">Our Services</h2>
<p class="abs section-lede" style="left:0;top:458px">Sed ut perspiciatis unde omnis iste natus error sit voluptatem accusantium doloremque laudantium, totam rem aperiam,</p>

<article class="abs service-card" style="left:59px">
  <div class="service-photo" role="img" aria-label="Photo of a presenter at a laptop facing a conference audience" style="background:linear-gradient(135deg,#c8502c,#3a2b33 55%,#1f2a3d)"></div>
  <h3 class="service-name">Virtual Organization</h3>
  <p class="service-text">Scusamus et iusto odio dignissimos ducimus molestias excepturi sint occaecati cupiditate non provident similique ...</p>
  <span class="btn-green">Read More</span>
</article>
<article class="abs service-card" style="left:213px">
  <div class="service-photo" role="img" aria-label="Photo of two business people shaking hands in a bright office" style="background:linear-gradient(135deg,#dfe8ee,#9fb0bf 50%,#5c6470)"></div>
  <h3 class="service-name">Business Consulting</h3>
  <p class="service-text">Scusamus et iusto odio dignissimos ducimus molestias excepturi sint occaecati cupiditate non provident similique ...</p>
  <span class="btn-green">Read More</span>
</article>
<article class="abs service-card" style="left:367px">
  <div class="service-photo" role="img" aria-label="Photo of two businessmen reviewing documents at a desk" style="background:linear-gradient(135deg,#cfdbe6,#6c8299 45%,#1e2a45)"></div>
  <h3 class="service-name">Event Planning</h3>
  <p class="service-text">Scusamus et iusto odio dignissimos ducimus molestias excepturi sint occaecati cupiditate non provident similique ...</p>
  <span class="btn-green">Read More</span>
</article>
<article class="abs service-card" style="left:521px">
  <div class="service-photo" role="img" aria-label="Photo of a passenger jet flying above clouds and a city" style="background:linear-gradient(180deg,#4e7bb5,#a9c6e4 55%,#6f8aa6)"></div>
  <h3 class="service-name">Travel Arrangements</h3>
  <p class="service-text">Scusamus et iusto odio dignissimos ducimus molestias excepturi sint occaecati cupiditate non provident similique ...</p>
  <span class="btn-green">Read More</span>
</article>

<section class="abs conclusion">
  <h3>Conclusion</h3>
  <p>At Quorvane, we are committed to become your virtual resource by providing quality, cutting edge services to expand your business virtually and save your valuable time. The time to act is now! Start increasing your bottom line...</p>
  <span class="act-btn">THE TIME TO ACT IS NOW!</span>
</section>

<h2 class="abs section-title" style="left:0;top:808px">What we do?</h2>
<p class="abs section-lede" style="left:0;top:853px">Sed ut perspiciatis unde omnis iste natus error sit voluptatem accusantium doloremque laudantium, totam rem aperiam,</p>

<div class="abs work-band"></div>
<div class="abs work-item" style="left:66px">
  <div class="work-ring"><div class="work-core">
    <svg width="22" height="22" viewBox="0 0 24 24"><circle cx="12" cy="12" r="6" fill="none" stroke="#c0442a" stroke-width="3"/><g stroke="#e07a2a" stroke-width="3"><path d="M12 2v4M12 18v4M2 12h4M18 12h4M5 5l3 3M16 16l3 3M19 5l-3 3M8 16l-3 3"/></g></svg>
  </div></div>
  <h4>Operations</h4>
  <p>Mara Quill is the registered agent and will supervise<br>all day to day operations until the time...</p>
  <p class="more">Read More+</p>
</div>
<div class="abs work-item" style="left:262px">
  <div class="work-ring"><div class="work-core">
    <svg width="22" height="20" viewBox="0 0 22 20"><path d="M1 1v18h20" fill="none" stroke="#c0442a" stroke-width="1.5"/><rect x="5" y="9" width="3" height="9" fill="#c0442a"/><rect x="10" y="5" width="3" height="13" fill="#e07a2a"/><rect x="15" y="8" width="3" height="10" fill="#c0442a"/></svg>
  </div></div>
  <h4>Marketing</h4>
  <p>Our target market is small business owners/ entre-<br>preneurs in the Dallas area between...</p>
  <p class="more">Read More+</p>
</div>
<div class="abs work-item" style="left:461px">
  <div class="work-ring"><div class="work-core">
    <svg width="22" height="20" viewBox="0 0 22 20"><rect x="1" y="1" width="20" height="13" rx="1" fill="#c0442a"/><rect x="3" y="3" width="16" height="9" fill="#e8866a"/><rect x="9" y="14" width="4" height="3" fill="#c0442a"/><rect x="6" y="17" width="10" height="2" fill="#c0442a"/></svg>
  </div></div>
  <h4>Competition</h4>
  <p>The world today is moving away from traditional ways<br>of doing business and toward utilizing...</p>
  <p class="more">Read More+</p>
</div>

<footer class="abs site-footer"></footer>
<div class="abs footer-col" style="left:59px">
  <h5>NEWSLETTER</h5>
  <p>Get our recent updates through your email id</p>
  <div class="field" style="margin-top:7px">Enter your Name</div>
  <div class="field">Enter your email id</div>
  <div class="subscribe">SUBSCRIBE NOW</div>
</div>
<div class="abs footer-col" style="left:281px">
  <h5>NAVIGATION</h5>
  <ul><li>Home</li><li>About us</li><li>Services</li><li>FAQ</li><li>Blog</li><li>Contact us</li></ul>
</div>
<div class="abs footer-col" style="left:403px">
  <h5>INFORMATION</h5>
  <ul><li>Terms &amp; Conditions</li><li>Privacy Policy</li><li>Site Map</li><li>Goals &amp; Objectives</li><li>Quorvane Tasks</li></ul>
</div>
<div class="abs footer-col" style="left:533px">
  <h5>CONTACT US</h5>
  <div class="contact-line"><svg width="7" height="9" viewBox="0 0 12 16"><path d="M6 0a6 6 0 0 0-6 6c0 4.5 6 10 6 10s6-5.5 6-10a6 6 0 0 0-6-6zm0 8.5A2.5 2.5 0 1 1 6 3.5a2.5 2.5 0 0 1 0 5z" fill="#8c8c8c"/></svg><span>4410 quorvane,Company suite<br>P.O.Box 508812, Dallas, Texas 75301</span></div>
  <div class="contact-line"><svg width="8" height="8" viewBox="0 0 24 24"><path d="M6.6 10.8a15 15 0 0 0 6.6 6.6l2.2-2.2a1 1 0 0 1 1-.25 11 11 0 0 0 3.6.6 1 1 0 0 1 1 1V20a1 1 0 0 1-1 1A17 17 0 0 1 3 4a1 1 0 0 1 1-1h3.5a1 1 0 0 1 1 1 11 11 0 0 0 .6 3.6 1 1 0 0 1-.25 1z" fill="#8c8c8c"/></svg><span>Phone: (555) 014-2290</span></div>
  <div class="contact-line"><svg width="8" height="7" viewBox="0 0 24 20"><rect x="1" y="1" width="22" height="18" fill="#8c8c8c"/><path d="M1 2l11 8 11-8" fill="none" stroke="#2b2b2b" stroke-width="2"/></svg><span>Email: info@quorvane.example</span></div>
</div>
<div class="abs footer-base">© Copyrights 2016. quorvane. All rights reserved.</div>

</body>
</html>
```